Flyer for Brightwell Table Provisions Company

Flyer Size: Double Sided 210mm * 148mm (Half a Sheet of Paper)
For your reference I have attached the logo and the web address is www.brightwelltableprovisions.com.
Specifications:
- Must contain the menu pricing chart, contact information, and hours of operation posted on the website.
- The menu must have an organization system from 1. Select Glaze through 4.Drinks. This will be the determining factor for selection. Graphic must be a mixture of creativity and function.
-The flyer can be identical on both sides (Not a determining factor)
-Incorporate the logo on both sides.
-The flyer does not have to be based on the website. (Not a determining factor)
My team will be handing these flyers out to HR Directors and Securities at Corporate offices.
Please let me know if you have any questions.
Updates
Project Deadline Extended
Reason: Website was not operational .
Brief has been updated and the website is up for your reference.
Target Market(s)
Corporate Office Catering. Secretary or HR director, usually a female.
Industry/Entity Type
Catering
Look and feel

```html
<!DOCTYPE html>
<html lang="en">
<head>
<meta charset="utf-8">
<title>Brightwell Table Provisions – Menu Flyer</title>
<link rel="stylesheet" href="https://fonts.googleapis.com/css2?family=Sansita:wght@800;900&family=Open+Sans:wght@700&display=swap">
<style>
:root{
  --parchment-light:#efe4cb;
  --parchment:#e4d4b2;
  --parchment-dark:#d6c29b;
  --ink:#4a1510;
  --menu-red:#7d1610;
  --band-brown:#3a1a0e;
  --accent-orange:#e8431a;
  --cream:#f1e2bd;
  --pattern-tone:#c9b188;
}
*{margin:0;padding:0;box-sizing:border-box}
html,body{width:846px;height:1200px;overflow:hidden}
body{font-family:"Sansita",Georgia,serif;color:var(--ink)}
.flyer{
  position:relative;width:846px;height:1200px;overflow:hidden;
  background:radial-gradient(ellipse at 50% 45%,var(--parchment-light) 0%,var(--parchment) 60%,var(--parchment-dark) 100%);
}
.pattern-band{position:absolute;left:0;width:846px;background:linear-gradient(var(--pattern-tone),#b89c70)}
.pattern-band.top{top:0;height:60px;opacity:.75}
.pattern-band.bottom{bottom:0;height:60px;background:linear-gradient(#d8c49c,#c3a97c)}
.brand{
  position:absolute;top:120px;left:0;width:846px;display:flex;justify-content:center;align-items:center;gap:18px;
}
.brand-dot{width:74px;height:74px;border-radius:50%;background:var(--accent-orange)}
.brand-name{font-weight:800;font-size:34px;line-height:1.05;color:var(--accent-orange);width:300px}
.menu-bar{position:absolute;top:253px;left:60px;width:726px;height:52px;background:var(--menu-red);
  color:var(--cream);font-family:"Open Sans",Arial,sans-serif;font-weight:700;font-size:20px;
  display:flex;align-items:center;justify-content:center;letter-spacing:.5px}
.bar-cap{position:absolute;top:253px;width:46px;height:52px;background:var(--band-brown)}
.bar-cap.left{left:0}.bar-cap.right{right:0}
.step{position:absolute}
.step-num{position:absolute;width:46px;height:46px;border-radius:50%;background:var(--menu-red);color:var(--cream);
  font-weight:900;font-size:26px;display:flex;align-items:center;justify-content:center}
.step-title{font-weight:900;font-size:22px;line-height:29px;letter-spacing:.3px}
.step-list{list-style:none;font-weight:800;font-size:19px;line-height:24.2px;color:var(--menu-red)}
.step-list li::before{content:"";display:inline-block;width:8px;height:8px;border-radius:50%;background:var(--menu-red);margin-right:8px;vertical-align:3px}
.step-list .note{padding-left:0}
.step-list .note::before{display:none}
.price-block{position:absolute;top:828px;left:0;width:846px;text-align:center}
.price-title{font-weight:900;font-size:22px}
.price-sub{font-weight:800;font-size:12px;margin-top:-2px}
.price-table{position:absolute;top:890px;left:37px;border-collapse:collapse;font-weight:900;color:var(--menu-red)}
.price-table th{text-align:left;font-size:18px;width:127px;line-height:24px;padding:0}
.price-table td{text-align:center;font-size:16px;width:64.2px;line-height:24px;border-left:2px solid #b9836e;padding:0}
.price-table td:last-child{border-right:2px solid #b9836e}
.contact{position:absolute;top:978px;left:0;width:846px;text-align:center}
.contact-title{font-weight:900;font-size:22px;line-height:28px}
.contact-line{font-weight:800;font-size:16px;line-height:23px}
.rule{position:absolute;top:1062px;left:0;width:846px;height:7px;background:var(--menu-red)}
.footer{position:absolute;top:1075px;left:0;width:846px;height:125px;background:var(--band-brown)}
.footer-url{position:absolute;top:1085px;left:0;width:846px;text-align:center;font-weight:900;font-size:27px;color:var(--cream);letter-spacing:.3px}
</style>
</head>
<body>
<main class="flyer">
  <div class="pattern-band top" role="img" aria-label="Decorative geometric border pattern"></div>

  <header class="brand">
    <span class="brand-dot"></span>
    <span class="brand-name">Brightwell Table Provisions</span>
  </header>

  <span class="bar-cap left"></span>
  <h1 class="menu-bar">MENU</h1>
  <span class="bar-cap right"></span>

  <section class="step" style="left:45px;top:330px">
    <span class="step-num" style="left:0;top:0">1</span>
    <div style="position:absolute;left:64px;top:-6px;width:320px">
      <h2 class="step-title">SELECT ROTISSERIE<br>CHICKEN GLAZE</h2>
      <ul class="step-list" style="margin-top:20px">
        <li>ORIGINAL</li><li>BARBECUE</li><li>HONEY</li><li>SPICY</li><li>CHIPOTLE</li>
        <li>CHIPOTLE-LIME</li><li>JAMAICAN JERK</li><li>TERIYAKI</li><li>BUFFALO</li>
        <li>BALSAMIC CHICKEN</li><li>HAWAIIAN</li><li>LEMON PEPPER ROSEMARY</li>
        <li>LEMONADE CHICKEN</li><li>LEMON ZEST</li><li>ORANGE</li><li>ORANGE AND ONION</li>
      </ul>
    </div>
  </section>

  <section class="step" style="left:456px;top:330px">
    <span class="step-num" style="left:0;top:0">2</span>
    <div style="position:absolute;left:64px;top:-6px;width:320px">
      <h2 class="step-title">SELECT SIDES</h2>
      <ul class="step-list">
        <li>CAESAR SALAD</li><li>FRIED RICE</li><li>WHITE RICE</li><li>MASHED POTATOES</li><li>HUMMUS &amp; PITA</li>
      </ul>
    </div>
  </section>

  <section class="step" style="left:456px;top:520px">
    <span class="step-num" style="left:0;top:0">3</span>
    <div style="position:absolute;left:64px;top:-6px;width:320px">
      <h2 class="step-title">SELECT DESSERT</h2>
      <ul class="step-list">
        <li>HAZELIA COVERED</li><li>CHOCOLATE CHIP COOKIES</li>
      </ul>
    </div>
  </section>

  <section class="step" style="left:456px;top:630px">
    <span class="step-num" style="left:0;top:0">4</span>
    <div style="position:absolute;left:64px;top:-6px;width:320px">
      <h2 class="step-title">SELECT DRINKS</h2>
      <ul class="step-list">
        <li>KOLO</li><li>PEPRA</li><li>SPARKLE</li><li>MESA ICE TEA</li>
        <li class="note">(ICED TEA &amp; LEMON TEA)</li><li>ELM SPRING WATER</li>
      </ul>
    </div>
  </section>

  <div class="price-block">
    <h2 class="price-title">AVERAGE PRICE</h2>
    <p class="price-sub">(with delivery and sides)</p>
  </div>
  <table class="price-table">
    <tr><th>PARTY SIZE:</th><td>10</td><td>20</td><td>30</td><td>40</td><td>50</td><td>60</td><td>80</td><td>100</td><td>150</td><td>200</td></tr>
    <tr><th>PRICE:</th><td>$105</td><td>$165</td><td>$225</td><td>$290</td><td>$330</td><td>$395</td><td>$515</td><td>$625</td><td>$940</td><td>$1,235</td></tr>
  </table>

  <address class="contact" style="font-style:normal">
    <h2 class="contact-title">CONTACT US</h2>
    <p class="contact-line">(555) 014-2290</p>
    <p class="contact-line">SALES@BRIGHTWELLTABLEPROVISIONS.COM</p>
  </address>

  <div class="rule"></div>
  <footer class="footer"></footer>
  <p class="footer-url">www.brightwelltableprovisions.com</p>
  <div class="pattern-band bottom" role="img" aria-label="Decorative geometric border pattern"></div>
</main>
</body>
</html>
```